Apricot Variety Sheet - Cedarline Orchard Growers

We are needing a variety sheet that we can hand out that will describe the different apricot vatieties we have available. The attached document has the name of the variety along with a description that will need to be on the sheet. We are looking for a modern, appealing way to display this information on 1 page (if needed, it can be front and back)
Updates

Apologies for the delay; we are overwhelmed with the great design options and will be sorting through them all (across our contests) to pick a collective. Thank you for your patience.

Target Market(s)

Growers and consumers

Industry/Entity Type

Agriculture

Requirements
Must have
• Easy to read
• Natural color palettes to emphasize the agricultural nature
• Clearly show washington as the origin in the title or at the top
Nice to have
• incorporate Apricots in the design

```html
<!DOCTYPE html>
<html lang="en">
<head>
<meta charset="utf-8">
<title>Washington Apricot Varieties – Cedarline Orchard Growers</title>
<link href="https://fonts.googleapis.com/css2?family=Nunito:wght@800;900&family=Montserrat:wght@400;600;700&display=swap" rel="stylesheet">
<style>
  :root{
    --bg-top:#bcbdbf;
    --bg-bottom:#a3a4a6;
    --paper:#ffffff;
    --green:#3cb54a;
    --green-light:#8cc63f;
    --green-card:rgba(140,198,63,.92);
    --green-dark:#1f8a3c;
    --apricot:#f6b567;
    --apricot-pale:#fde6c8;
    --text-light:#ffffff;
  }
  *{margin:0;padding:0;box-sizing:border-box}
  html,body{width:1200px;height:898px;overflow:hidden}
  body{background:linear-gradient(180deg,var(--bg-top),var(--bg-bottom));font-family:"Montserrat",sans-serif}
  .stage{position:absolute;left:0;top:0;width:1365px;height:1022px;transform:scale(.87912);transform-origin:0 0}
  .sheet{position:absolute;background:var(--paper);overflow:hidden;box-shadow:0 2px 8px rgba(0,0,0,.15)}
  .sheet--front{left:57px;top:88px;width:614px;height:792px}
  .sheet--back{left:709px;top:162px;width:611px;height:791px}
  .shape{position:absolute;left:0;width:100%}
  .backdrop{position:absolute;left:0;width:100%}
  .sheet--front .backdrop{top:170px;height:580px;
    background:radial-gradient(ellipse 45% 35% at 20% 30%,var(--apricot) 0%,rgba(246,181,103,0) 100%),
      radial-gradient(ellipse 40% 30% at 75% 55%,var(--apricot) 0%,rgba(246,181,103,0) 100%),
      radial-gradient(ellipse 50% 35% at 40% 80%,var(--apricot-pale) 0%,rgba(253,230,200,0) 100%),#fbf3ea}
  .sheet--back .backdrop{top:0;height:590px;
    background:radial-gradient(ellipse 40% 30% at 80% 20%,var(--apricot) 0%,rgba(246,181,103,0) 100%),
      radial-gradient(ellipse 45% 30% at 20% 55%,var(--apricot-pale) 0%,rgba(253,230,200,0) 100%),
      radial-gradient(ellipse 40% 30% at 70% 70%,var(--apricot) 0%,rgba(246,181,103,0) 100%),#fdf7f0}
  .brand{position:absolute;display:flex;align-items:center;gap:12px;color:var(--green-dark);font-family:"Nunito",sans-serif;font-weight:900}
  .brand__dot{border-radius:50%;background:var(--green-dark);flex:none}
  .brand--header{left:133px;top:28px;font-size:22px;line-height:22px}
  .brand--header .brand__dot{width:78px;height:78px}
  .brand--footer{left:203px;top:704px;font-size:15.5px;line-height:16px}
  .brand--footer .brand__dot{width:50px;height:50px}
  .sheet-title{position:absolute;left:0;width:100%;top:135px;text-align:center;color:var(--text-light);font-family:"Nunito",sans-serif;font-weight:900;font-size:26px;letter-spacing:1.5px}
  .variety{position:absolute;color:var(--text-light)}
  .variety__shape{position:absolute;inset:0;width:100%;height:100%}
  .variety__num{position:absolute;left:-18px;top:22px;width:32px;height:32px;border-radius:50%;background:var(--green-light);border:2px solid #fff;color:#fff;font-family:"Nunito",sans-serif;font-weight:900;font-size:16px;display:flex;align-items:center;justify-content:center}
  .variety__name{position:absolute;left:23px;top:6px;color:var(--green-dark);font-family:"Nunito",sans-serif;font-weight:900;font-size:24px;letter-spacing:1px}
  .variety__name--sm{font-size:19px;top:12px}
  .variety__text{position:absolute;left:9px;right:4px;top:52px;font-size:11.6px;line-height:21px;font-weight:400}
  .variety__text--fine{font-size:10.8px;line-height:20.3px}
  .variety__text strong{font-weight:700}
  .fruit{position:absolute;top:600px;height:100px;border-radius:50%}
  .fruit--halves{left:46px;width:130px;background:radial-gradient(circle at 45% 45%,#f6a53a,#ef8b25 60%,rgba(239,139,37,0) 72%)}
  .fruit--pile{left:211px;width:165px;background:radial-gradient(circle at 50% 50%,#f7c05e,#eda449 60%,rgba(237,164,73,0) 72%)}
  .fruit--single{left:416px;width:110px;background:radial-gradient(circle at 50% 50%,#f7a74a,#ec8a2d 60%,rgba(236,138,45,0) 72%)}
  .fruit-divider{position:absolute;top:632px;width:1px;height:36px;background:var(--green-light)}
</style>
</head>
<body>
<div class="stage">

  <section class="sheet sheet--front">
    <div class="backdrop" role="img" aria-label="Soft photo of ripe apricots behind the variety cards"></div>
    <svg class="shape" style="top:0;height:180px" viewBox="0 0 614 180" preserveAspectRatio="none" aria-hidden="true">
      <defs><linearGradient id="hdr" x1="0" x2="1"><stop offset="0" stop-color="#8cc63f"/><stop offset="1" stop-color="#39b54a"/></linearGradient></defs>
      <rect width="614" height="176" fill="url(#hdr)"/>
      <path d="M0,0 C120,175 470,150 614,0 Z" fill="#fff"/>
    </svg>
    <div class="brand brand--header"><span class="brand__dot"></span><span>Cedarline Orchard<br>Growers</span></div>
    <h1 class="sheet-title">WASHINGTON APRICOT VARIETIES</h1>

    <article class="variety" style="left:34px;top:194px;width:266px;height:156px">
      <svg class="variety__shape" viewBox="0 0 266 156" preserveAspectRatio="none" aria-hidden="true"><path d="M0,0 H266 Q150,32 0,38 Z" fill="#fff" opacity=".85"/><path d="M0,38 Q150,32 266,0 V156 H0 Z" fill="var(--green-card)"/></svg>
      <span class="variety__num">1</span><h2 class="variety__name">Rival</h2>
      <p class="variety__text variety__text--fine">Great flavor with a fine, firm texture distinguishes this large oval-shaped apricot. The skin is light orange witha red blush. The flesh is a lush deep orange color. <strong>Available early July- early August.</strong></p>
    </article>
    <article class="variety" style="left:334px;top:194px;width:266px;height:156px">
      <svg class="variety__shape" viewBox="0 0 266 156" preserveAspectRatio="none" aria-hidden="true"><path d="M0,0 H266 Q150,32 0,38 Z" fill="#fff" opacity=".85"/><path d="M0,38 Q150,32 266,0 V156 H0 Z" fill="var(--green-card)"/></svg>
      <span class="variety__num">2</span><h2 class="variety__name">Robada</h2>
      <p class="variety__text">This jumbo apricot has a delicious floral flavor with a firm texture. Bright orange, with a deep red blush over nearly half its surface. <strong>Available early June.</strong></p>
    </article>
    <article class="variety" style="left:34px;top:390px;width:266px;height:160px">
      <svg class="variety__shape" viewBox="0 0 266 160" preserveAspectRatio="none" aria-hidden="true"><path d="M0,0 H266 Q150,32 0,38 Z" fill="#fff" opacity=".85"/><path d="M0,38 Q150,32 266,0 V160 H0 Z" fill="var(--green-card)"/></svg>
      <span class="variety__num">3</span><h2 class="variety__name variety__name--sm">Perfection</h2>
      <p class="variety__text">This classic large oval apricot is deep orange with an oblong shape and firm texture. The flesh is a yellow/orange color that is very sweet and full of flavor. <strong>Available mid July - mid August.</strong></p>
    </article>
    <article class="variety" style="left:334px;top:390px;width:266px;height:160px">
      <svg class="variety__shape" viewBox="0 0 266 160" preserveAspectRatio="none" aria-hidden="true"><path d="M0,0 H266 Q150,32 0,38 Z" fill="#fff" opacity=".85"/><path d="M0,38 Q150,32 266,0 V160 H0 Z" fill="var(--green-card)"/></svg>
      <span class="variety__num">4</span><h2 class="variety__name variety__name--sm">Patterson</h2>
      <p class="variety__text variety__text--fine">Great flavor with a fine, firm texture distinguishes this large oval-shaped apricot. The skin is light orange witha red blush. The flesh is a lush deep orange color. <strong>Available early July- early August.</strong></p>
    </article>
    <article class="variety" style="left:34px;top:575px;width:266px;height:165px">
      <svg class="variety__shape" viewBox="0 0 266 165" preserveAspectRatio="none" aria-hidden="true"><path d="M0,0 H266 Q150,32 0,38 Z" fill="#fff" opacity=".85"/><path d="M0,38 Q150,32 266,0 V165 H0 Z" fill="var(--green-card)"/></svg>
      <span class="variety__num">5</span><h2 class="variety__name">Tomcot</h2>
      <p class="variety__text">Tangy, sweet flavor with a firm texture. This oval apricot is light orange with a slight blush color. The flesh is a dark orange. <strong>Available late June – late July.</strong></p>
    </article>
    <article class="variety" style="left:334px;top:575px;width:266px;height:168px">
      <svg class="variety__shape" viewBox="0 0 266 168" preserveAspectRatio="none" aria-hidden="true"><path d="M0,0 H266 Q150,32 0,38 Z" fill="#fff" opacity=".85"/><path d="M0,38 Q150,32 266,0 V168 H0 Z" fill="var(--green-card)"/></svg>
      <span class="variety__num">6</span><h2 class="variety__name">Goldrich</h2>
      <p class="variety__text">This apricot is round with a bright orange skin color and a deep orange flesh. It has a mild, sweet flavor with a firm texture.<br><strong>Available early July – mid August</strong></p>
    </article>

    <svg class="shape" style="top:740px;height:52px" viewBox="0 0 614 52" preserveAspectRatio="none" aria-hidden="true">
      <defs><linearGradient id="ftrA" x1="0" x2="1"><stop offset="0" stop-color="#39b54a"/><stop offset="1" stop-color="#8cc63f"/></linearGradient></defs>
      <rect width="614" height="52" fill="#fff"/>
      <path d="M0,8 C200,20 430,40 614,18 V52 H0 Z" fill="url(#ftrA)"/>
    </svg>
  </section>

  <section class="sheet sheet--back">
    <div class="backdrop" role="img" aria-label="Soft photo of ripe apricots behind the variety cards"></div>

    <article class="variety" style="left:31px;top:32px;width:265px;height:160px">
      <svg class="variety__shape" viewBox="0 0 265 160" preserveAspectRatio="none" aria-hidden="true"><path d="M0,0 H265 Q150,32 0,38 Z" fill="#fff" opacity=".85"/><path d="M0,38 Q150,32 265,0 V160 H0 Z" fill="var(--green-card)"/></svg>
      <span class="variety__num">7</span><h2 class="variety__name variety__name--sm">Casselbrite</h2>
      <p class="variety__text variety__text--fine" style="top:50px">This medium sized apricot is golden orange with a slight red blush. It has a mild sweet-tart flavor that is good for eating out of hand. <strong>Available late June- early July.</strong></p>
    </article>
    <article class="variety" style="left:331px;top:32px;width:266px;height:160px">
      <svg class="variety__shape" viewBox="0 0 266 160" preserveAspectRatio="none" aria-hidden="true"><path d="M0,0 H266 Q150,32 0,38 Z" fill="#fff" opacity=".85"/><path d="M0,38 Q150,32 266,0 V160 H0 Z" fill="var(--green-card)"/></svg>
      <span class="variety__num">8</span><h2 class="variety__name variety__name--sm">Goldbar</h2>
      <p class="variety__text variety__text--fine" style="top:50px">Moderately juicy, this large oval-shaped apricot has a light yellow-orange with a reddish blush. The flesh is firm, meaty, and has a light orange color. <strong>Available late June – end of July.</strong></p>
    </article>
    <article class="variety" style="left:31px;top:232px;width:265px;height:159px">
      <svg class="variety__shape" viewBox="0 0 265 159" preserveAspectRatio="none" aria-hidden="true"><path d="M0,0 H265 Q150,32 0,38 Z" fill="#fff" opacity=".85"/><path d="M0,38 Q150,32 265,0 V159 H0 Z" fill="var(--green-card)"/></svg>
      <span class="variety__num">9</span><h2 class="variety__name variety__name--sm">Sweet Juillet</h2>
      <p class="variety__text">This special variety has a unique, sweet flavor with a juicy flesh. It is bright orange in color with a bright orange flesh. <strong>Available through July.</strong></p>
    </article>
    <article class="variety" style="left:331px;top:232px;width:266px;height:159px">
      <svg class="variety__shape" viewBox="0 0 266 159" preserveAspectRatio="none" aria-hidden="true"><path d="M0,0 H266 Q150,32 0,38 Z" fill="#fff" opacity=".85"/><path d="M0,38 Q150,32 266,0 V159 H0 Z" fill="var(--green-card)"/></svg>
      <span class="variety__num">10</span><h2 class="variety__name variety__name--sm">Tasty Rich</h2>
      <p class="variety__text variety__text--fine" style="top:50px">This early variety is light yellow-orange colored with a firm texture. Very juicy with an enticing flavor.<br><strong>Available through June.</strong></p>
    </article>
    <article class="variety" style="left:31px;top:417px;width:265px;height:169px">
      <svg class="variety__shape" viewBox="0 0 265 169" preserveAspectRatio="none" aria-hidden="true"><path d="M0,0 H265 Q150,32 0,38 Z" fill="#fff" opacity=".85"/><path d="M0,38 Q150,32 265,0 V169 H0 Z" fill="var(--green-card)"/></svg>
      <span class="variety__num">11</span><h2 class="variety__name variety__name--sm">Goldstrick</h2>
      <p class="variety__text">A larger apricot with light orange, blushed skin. Firm texture with a slight tart taste until fully ripened, then very sweet. <strong>Available mid June - mid July.</strong></p>
    </article>
    <article class="variety" style="left:331px;top:417px;width:266px;height:169px">
      <svg class="variety__shape" viewBox="0 0 266 169" preserveAspectRatio="none" aria-hidden="true"><path d="M0,0 H266 Q150,32 0,38 Z" fill="#fff" opacity=".85"/><path d="M0,38 Q150,32 266,0 V169 H0 Z" fill="var(--green-card)"/></svg>
      <span class="variety__num">12</span><h2 class="variety__name">Riland</h2>
      <p class="variety__text">Very aromatic and sweet, this apricot is orange with a red blush. It has a yellow-orange colored flesh and a round shape.<br><strong>&nbsp;Available mid-June to end of July.</strong></p>
    </article>

    <div class="fruit fruit--halves" role="img" aria-label="Apricot halves with leaves"></div>
    <span class="fruit-divider" style="left:193px"></span>
    <div class="fruit fruit--pile" role="img" aria-label="Pile of fresh apricots"></div>
    <span class="fruit-divider" style="left:394px"></span>
    <div class="fruit fruit--single" role="img" aria-label="Single apricot with a leaf"></div>

    <div class="brand brand--footer"><span class="brand__dot"></span><span>Cedarline Orchard<br>Growers</span></div>

    <svg class="shape" style="top:744px;height:47px" viewBox="0 0 611 47" preserveAspectRatio="none" aria-hidden="true">
      <defs><linearGradient id="ftrB" x1="0" x2="1"><stop offset="0" stop-color="#39b54a"/><stop offset="1" stop-color="#8cc63f"/></linearGradient></defs>
      <path d="M0,4 C200,18 430,34 611,14 V47 H0 Z" fill="url(#ftrB)"/>
    </svg>
  </section>

</div>
</body>
</html>
```